Workvane Background Design

Need to develop a Workvane Background picture for my profile. The components I want in there are:
1) Name: Mohit Varma
2) Key Skills: Strategy, Innovation, Execution, Growth and Leadership
3) A photograph (an action photograph) The attached photograph is an example.
A black background would be ideal.

The design should meet the Workvane background size requirements.

The background should reinforce an image of a thinking person but equally capable of implementing.

Leadership

```html
<!DOCTYPE html>
<html lang="en">
<head>
<meta charset="utf-8">
<title>Workvane Background Design</title>
<link href="https://fonts.googleapis.com/css2?family=Questrial&family=Arimo:wght@400;700&display=swap" rel="stylesheet">
<style>
  :root {
    --stage-light: #f7f7f7;
    --stage-edge: #dedede;
    --ink-black: #000000;
    --caption-white: #ffffff;
    --nav-top: #6a6a6a;
    --nav-bottom: #3c3c3c;
    --nav-icon: #d8d8d8;
    --search-field: #ffffff;
    --search-hint: #8a8a8a;
    --search-button: #2b6db5;
    --menu-button: #5b5b5b;
    --page-grey: #dcdcdc;
    --panel-white: #ffffff;
    --panel-line: #c9c9c9;
    --scroll-track: #f0f0f0;
    --scroll-thumb: #c4c4c4;
    --banner-dark: #05080f;
    --ember-deep: #2e0a03;
    --ember-mid: #8a2c08;
    --ember-bright: #d9760f;
    --glow-gold: #f7b43a;
    --glow-white: #fff4da;
    --headline: #fbe9d0;
    --headline-glow: #ff8a1e;
  }
  * { margin: 0; padding: 0; box-sizing: border-box; }
  html, body {
    width: 1200px;
    height: 848px;
    overflow: hidden;
  }
  .canvas {
    position: relative;
    width: 1200px;
    height: 848px;
    overflow: hidden;
    background: radial-gradient(ellipse 760px 520px at 600px 380px, var(--stage-light) 55%, var(--stage-edge) 100%);
  }
  .corner-band { position: absolute; left: 0; top: 0; }

  .caption-bar {
    position: absolute;
    left: 0;
    top: 793px;
    width: 1200px;
    height: 55px;
    background: var(--ink-black);
  }
  .caption-title {
    position: absolute;
    left: 63px;
    top: 14px;
    font-family: "Questrial", sans-serif;
    font-size: 17px;
    color: var(--caption-white);
    white-space: nowrap;
  }

  .browser {
    position: absolute;
    left: 124px;
    top: 77px;
    width: 951px;
    height: 661px;
    background: var(--page-grey);
    overflow: hidden;
  }
  .top-nav {
    position: absolute;
    left: 0;
    top: 0;
    width: 940px;
    height: 31px;
    background: linear-gradient(180deg, var(--nav-top), var(--nav-bottom));
    font-family: "Arimo", sans-serif;
  }
  .brand-name {
    position: absolute;
    left: 106px;
    top: 7px;
    font-family: "Questrial", sans-serif;
    font-size: 14px;
    color: var(--caption-white);
  }
  .menu-button {
    position: absolute;
    left: 261px;
    top: 5px;
    width: 30px;
    height: 21px;
    background: var(--menu-button);
    border-radius: 2px 0 0 2px;
  }
  .search-field {
    position: absolute;
    left: 291px;
    top: 5px;
    width: 257px;
    height: 21px;
    background: var(--search-field);
    font-size: 10px;
    color: var(--search-hint);
    padding: 5px 0 0 7px;
    white-space: nowrap;
    overflow: hidden;
  }
  .search-button {
    position: absolute;
    left: 553px;
    top: 5px;
    width: 36px;
    height: 21px;
    background: var(--search-button);
    border-radius: 2px;
  }
  .advanced-link {
    position: absolute;
    left: 597px;
    top: 10px;
    font-size: 9px;
    color: var(--nav-icon);
  }
  .nav-icons { position: absolute; left: 700px; top: 6px; }

  .profile-banner {
    position: absolute;
    left: 0;
    top: 31px;
    width: 940px;
    height: 295px;
    background: var(--banner-dark);
    overflow: hidden;
  }
  .banner-scene {
    position: absolute;
    left: 0;
    top: 0;
    width: 500px;
    height: 295px;
    background:
      radial-gradient(ellipse 110px 90px at 330px 80px, rgba(217,118,15,0.45), transparent 70%),
      radial-gradient(ellipse 180px 150px at 110px 110px, var(--ember-mid), transparent 75%),
      linear-gradient(180deg, var(--ember-deep) 0%, #4e1806 55%, #8a4512 78%, #6a2c0a 100%);
    -webkit-mask-image: linear-gradient(90deg, #000 78%, transparent 100%);
            mask-image: linear-gradient(90deg, #000 78%, transparent 100%);
  }
  .banner-light {
    position: absolute;
    right: 0;
    top: 0;
    width: 120px;
    height: 295px;
    background:
      radial-gradient(ellipse 16px 150px at 8px 100px, var(--glow-white), rgba(247,180,58,0.6) 50%, transparent 90%),
      radial-gradient(ellipse 90px 140px at 70px 140px, rgba(247,180,58,0.65), rgba(90,50,10,0.5) 60%, transparent 100%),
      linear-gradient(180deg, #1a1206 0%, #3b2408 50%, #7a4a12 100%);
  }
  .skills-headline {
    position: absolute;
    font-family: "Questrial", sans-serif;
    font-style: italic;
    font-size: 19px;
    color: var(--headline);
    text-shadow: 0 0 5px var(--headline-glow), 0 0 12px rgba(255,138,30,0.55);
    white-space: nowrap;
  }
  .skills-line-one { left: 289px; top: 68px; }
  .skills-line-two { left: 546px; top: 94px; }
  .accent-rule {
    position: absolute;
    left: 778px;
    top: 114px;
    width: 54px;
    height: 1px;
    background: linear-gradient(90deg, rgba(247,180,58,0), var(--glow-gold));
  }

  .panel {
    position: absolute;
    background: var(--panel-white);
    border: 1px solid var(--panel-line);
  }
  .profile-card { left: 108px; top: 179px; width: 725px; height: 207px; }
  .profile-photo {
    position: absolute;
    left: -1px;
    top: -1px;
    width: 179px;
    height: 179px;
    background: var(--ink-black);
  }
  .main-column { left: 108px; top: 394px; width: 481px; height: 280px; }
  .main-column::before {
    content: "";
    position: absolute;
    left: 0;
    top: 0;
    width: 53px;
    height: 1px;
    background: var(--panel-line);
  }
  .side-column { left: 595px; top: 394px; width: 238px; height: 280px; }

  .scrollbar {
    position: absolute;
    left: 940px;
    top: 0;
    width: 11px;
    height: 661px;
    background: var(--scroll-track);
  }
  .scroll-thumb {
    position: absolute;
    left: 2px;
    top: 13px;
    width: 7px;
    height: 223px;
    background: var(--scroll-thumb);
  }
</style>
</head>
<body>
  <main class="canvas">
    <svg class="corner-band" width="230" height="110" viewBox="0 0 230 110" aria-hidden="true">
      <polygon points="0,36 154,0 221,0 0,103" fill="var(--ink-black)"/>
    </svg>

    <section class="browser">
      <header class="top-nav">
        <span class="brand-name">Workvane</span>
        <span class="menu-button">
          <svg width="30" height="21" viewBox="0 0 30 21" aria-hidden="true">
            <g stroke="#d0d0d0" stroke-width="1.5"><line x1="7" y1="7" x2="17" y2="7"/><line x1="7" y1="10.5" x2="17" y2="10.5"/><line x1="7" y1="14" x2="17" y2="14"/></g>
            <polygon points="21,9 26,9 23.5,12" fill="#d0d0d0"/>
          </svg>
        </span>
        <span class="search-field">Search for people, jobs, companies, and more...</span>
        <span class="search-button">
          <svg width="36" height="21" viewBox="0 0 36 21" aria-hidden="true">
            <circle cx="17" cy="9.5" r="3.5" fill="none" stroke="#fff" stroke-width="1.6"/>
            <line x1="19.5" y1="12" x2="22" y2="14.5" stroke="#fff" stroke-width="1.8"/>
          </svg>
        </span>
        <span class="advanced-link">Advanced</span>
        <svg class="nav-icons" width="240" height="20" viewBox="0 0 240 20" aria-hidden="true">
          <rect x="5" y="4" width="15" height="11" fill="none" stroke="var(--nav-icon)" stroke-width="1.4"/>
          <polyline points="5,4 12.5,10 20,4" fill="none" stroke="var(--nav-icon)" stroke-width="1.4"/>
          <line x1="42" y1="2" x2="42" y2="17" stroke="var(--nav-icon)" stroke-width="1.6"/>
          <polygon points="43,3 54,3 51,7 54,11 43,11" fill="var(--nav-icon)"/>
          <circle cx="82" cy="7" r="4" fill="var(--nav-icon)"/>
          <path d="M75 17 Q82 9 89 17 Z" fill="var(--nav-icon)"/>
          <g stroke="var(--nav-icon)" stroke-width="1.6"><line x1="72" y1="6" x2="72" y2="12"/><line x1="69" y1="9" x2="75" y2="9"/></g>
          <rect x="114" y="2" width="15" height="15" fill="var(--nav-icon)"/>
          <circle cx="121.5" cy="8" r="3" fill="#9a9a9a"/>
          <path d="M116 17 Q121.5 10 127 17 Z" fill="#9a9a9a"/>
        </svg>
      </header>

      <div class="profile-banner">
        <div class="banner-scene" role="img" aria-label="Action photograph of the speaker at a wooden podium pointing upward, set against glowing warm light bulbs"></div>
        <div class="banner-light" role="img" aria-label="Bright golden light beam bursting through a dark lens-like surface"></div>
        <p class="skills-headline skills-line-one">Strategy, Innovation, Execution,</p>
        <p class="skills-headline skills-line-two">Growth and Leadership</p>
        <span class="accent-rule"></span>
      </div>

      <div class="panel profile-card">
        <div class="profile-photo" role="img" aria-label="Profile photo placeholder"></div>
      </div>
      <div class="panel main-column"></div>
      <div class="panel side-column"></div>

      <div class="scrollbar">
        <svg width="11" height="11" viewBox="0 0 11 11" aria-hidden="true"><polygon points="3,7 8,7 5.5,4" fill="#777"/></svg>
        <span class="scroll-thumb"></span>
      </div>
    </section>

    <footer class="caption-bar">
      <p class="caption-title">Workvane Background Design</p>
    </footer>
  </main>
</body>
</html>
```